B2B flyer solution for charging infrastructures (One-Pager Din A4, double-sided)

We need a professional design for our flyer in format Din A4/both sides.
Attached you will find the content for the flyer, but we are looking for a modern, professional design.

Some background/context information:
- the product is about a solution for charging and billing of charging infrastructures (for electric cars) in companies
- target group: companies, esp. facility managers, fleet managers, controlling, CTO, CEO
- should be printed and available online
- our website (and most of our current design work): https://wendo-kraft.de

In the files you will find:
- photos of reference implementations of our solution (should be included in the flyer)
- stock photos (we are using the one you will find in the current flyer on our presentations, maybe you can use it too to keep some corporate identity.
- our logo
- the current flyer as PDF and as PowerPoint
- a sample presentation we also need for customer communication

It would be nice if the design will align with the existing design work, but bring fresh aspects and will be up-to-date and professional.

Target Market(s)

B2B, companies, fleet managers, facility managers, CTO, CIO

Industry/Entity Type

Enterprises, Charging Solutions for Electric Vehicles

Requirements
Nice to have
• Bright, light design, clean, readable

```html
<!DOCTYPE html>
<html lang="de">
<head>
<meta charset="utf-8">
<title>wendo-kraft Professional – Flyer</title>
<link rel="stylesheet" href="https://fonts.googleapis.com/css2?family=Exo+2:wght@400;500;700;800&family=Poppins:wght@400;500;600;700&display=swap">
<style>
  :root{
    --pink:#e5168e;
    --purple:#7e4cc8;
    --violet:#9a37c0;
    --ink:#1b1c2a;
    --text:#222230;
    --paper:#f6f6f8;
    --stage:#bdbdbd;
    --line:#c9c9d2;
    --brand-grad:linear-gradient(90deg,var(--pink),var(--purple));
  }
  *{box-sizing:border-box;margin:0;padding:0}
  html,body{width:1200px;height:877px;overflow:hidden}
  body{background:var(--stage);font-family:"Poppins",sans-serif;color:var(--text);position:relative}
  .page-label{position:absolute;top:44px;width:535px;text-align:center;color:#fff;font:600 20px "Poppins",sans-serif}
  .page{position:absolute;top:85px;width:535px;height:756px;background:var(--paper);overflow:hidden;box-shadow:0 4px 14px rgba(0,0,0,.35)}
  .page--front{left:58px}
  .page--back{left:613px}
  .abs{position:absolute}
  .hero-art{position:absolute;left:0;top:0}
  .brand-name{position:absolute;left:20px;top:72px;font:500 30px "Exo 2",sans-serif;color:var(--ink);letter-spacing:-.5px;display:flex;align-items:center;gap:8px;white-space:nowrap}
  .brand-dot{width:14px;height:14px;border-radius:50%;background:var(--pink)}
  .display{font-family:"Exo 2",sans-serif;font-weight:800;color:#fff;text-transform:uppercase;white-space:nowrap}

  /* front */
  .front-band{left:0;top:129px;width:330px;height:91px;background:var(--pink)}
  .front-title{left:18px;top:132px;font-size:35px;line-height:38px;letter-spacing:.3px}
  .tagline{left:21px;top:236px;border-left:3px solid var(--violet);padding-left:18px;font:400 17px/19.5px "Exo 2",sans-serif;color:var(--ink)}
  .claim{left:21px;top:315px;width:492px;border-radius:8px;overflow:hidden}
  .claim-main{background:var(--ink);color:#fff;text-align:center;font:500 15.5px/20.5px "Exo 2",sans-serif;padding:8px 10px 7px}
  .claim-sub{background:var(--brand-grad);color:#fff;text-align:center;font:400 12.5px/28px "Exo 2",sans-serif}
  .pill{left:21px;top:418px;background:var(--brand-grad);color:#fff;font:700 10px/14px "Poppins",sans-serif;padding:0 7px;border-radius:7px}
  .services{left:21px;top:436px;width:232px;list-style:none}
  .services li{position:relative;padding-left:15px;font-size:10px;line-height:12.8px;margin-bottom:6.5px}
  .services li::before,.checklist li::before{content:"";position:absolute;left:0;top:3px;width:7px;height:7px;border-radius:50%;background:var(--violet);box-shadow:inset 0 0 0 2px var(--violet),inset 0 0 0 3px #fff}
  .benefit-box{left:21px;top:579px;width:240px;height:113px;border:1px solid var(--line);border-radius:5px;background:#fff;overflow:hidden}
  .benefit-head{background:var(--brand-grad);color:#fff;font:600 10px/28px "Poppins",sans-serif;letter-spacing:-.2px;padding-left:9px;white-space:nowrap}
  .dotlist{list-style:none;font-size:8.8px;line-height:12.3px;padding:8px 6px 0 8px}
  .dotlist li{position:relative;padding-left:6px}
  .dotlist li::before{content:"•";position:absolute;left:0}
  .contact-box{left:276px;top:418px;width:237px;height:274px;border:1px solid var(--line);border-radius:6px;background:#fff;overflow:hidden}
  .photo{display:block;background:linear-gradient(135deg,#6f7276,#3a3c40 45%,#8a8c83 70%,#5c5e58)}
  .contact-photo{width:100%;height:134px}
  .section-head{font:700 11px/14px "Poppins",sans-serif;color:var(--pink);text-transform:uppercase}
  .contact-body{padding:9px 8px 0 10px}
  .contact-body p{font-size:8.8px;line-height:11.5px;margin-top:5px}
  .phone{display:flex;align-items:center;gap:6px;margin-top:8px;font:700 14.5px "Poppins",sans-serif;color:var(--ink);white-space:nowrap}
  .web-line{display:flex;align-items:center;gap:3px;margin-top:6px;font:600 7.8px "Poppins",sans-serif;color:var(--ink);white-space:nowrap}
  .footer-line{left:24px;top:714px;font:700 11.5px/16px "Poppins",sans-serif;color:var(--ink);white-space:nowrap}

  /* back */
  .back-band{left:0;top:121px;width:400px;height:51px;background:var(--pink)}
  .back-title{left:18px;top:131px;font-size:21px;letter-spacing:.3px}
  .back-dark{left:0;top:172px;width:535px;height:39px;background:var(--ink)}
  .back-sub{left:20px;top:181px;border-left:3px solid var(--pink);padding-left:17px;font:400 16.5px/20px "Exo 2",sans-serif;color:#fff}
  .billing-head{left:0;top:222px;width:535px;text-align:center;font:700 14px "Poppins",sans-serif;color:var(--ink)}
  .target{position:absolute;top:254px;width:120px;text-align:center;font:500 12px/14px "Poppins",sans-serif;color:var(--ink)}
  .target-icon{width:66px;height:66px;margin:0 auto 5px;border-radius:50%;background:linear-gradient(135deg,var(--pink),var(--purple));display:flex;align-items:center;justify-content:center}
  .divider{position:absolute;top:255px;width:1px;height:95px;background:var(--line)}
  .col-left{left:20px;top:396px;width:252px}
  .col-left p{font-size:10px;line-height:12.9px;margin-top:6px}
  .checklist{list-style:none;margin-top:5px}
  .checklist li{position:relative;padding-left:13px;font:500 9.8px/18px "Poppins",sans-serif;color:var(--ink);white-space:nowrap}
  .checklist li::before{top:5.5px}
  .ref-photo{position:absolute;top:572px;width:116px;height:118px;border:1px solid var(--line);border-radius:3px}
  .back-footer{left:20px;top:712px;font:700 11.5px/14px "Poppins",sans-serif;color:var(--ink);white-space:nowrap}
  .col-right{left:276px;top:366px;width:238px;height:400px;border:1px solid var(--line);border-bottom:none;border-radius:6px 6px 0 0;background:#fff;padding:22px 12px 0 14px}
  .col-right p{font-size:8.6px;line-height:11.2px;margin-top:6px}
  .small-list{list-style:none;font-size:8.6px;line-height:11.2px;margin-top:8px}
  .small-list li{position:relative;padding-left:5px}
  .small-list li::before{content:"•";position:absolute;left:0}
  .col-right .section-head + p{margin-top:7px}
  .gap{margin-top:20px}
</style>
</head>
<body>

<div class="page-label" style="left:58px">Front Page</div>
<div class="page-label" style="left:613px">Back Page</div>

<section class="page page--front">
  <svg class="hero-art" width="535" height="756" viewBox="0 0 535 756">
    <defs>
      <linearGradient id="ringF" x1="0" y1="0" x2="1" y2="0">
        <stop offset="0" stop-color="#e5168e"/><stop offset="1" stop-color="#7e4cc8"/>
      </linearGradient>
      <radialGradient id="photoF" cx=".65" cy=".55" r=".6">
        <stop offset="0" stop-color="#3aa6ff"/><stop offset=".4" stop-color="#1d55d8"/>
        <stop offset=".75" stop-color="#c9d8ee"/><stop offset="1" stop-color="#eef2f8"/>
      </radialGradient>
    </defs>
    <circle cx="451" cy="69" r="234" fill="url(#ringF)"/>
    <circle cx="451" cy="69" r="212" fill="url(#photoF)" role="img" aria-label="Foto: Ladestecker an einem Elektroauto mit blau leuchtender Ladebuchse"/>
  </svg>

  <div class="brand-name"><span class="brand-dot"></span>wendo-kraft.de</div>

  <div class="abs front-band"></div>
  <h1 class="abs display front-title">Wendo-Kraft<br>Professional</h1>

  <p class="abs tagline">die maßgeschneiderte<br>B2B-Abrechnungslösung<br>für Elektromobilität</p>

  <div class="abs claim">
    <div class="claim-main">Lade-Infrastruktur-Abrechnungslösungen für Unternehmen,<br>damit Lade-Infrastruktur Erträge statt Kosten produziert.</div>
    <div class="claim-sub">So wird Lade-Infrastruktur von einer Kostenstelle zu einem Profitcenter.</div>
  </div>

  <span class="abs pill">LEISTUNGEN:</span>
  <ul class="abs services">
    <li>Vielseitige Abrechnungsmöglichkeiten für Fuhrpark, Mitarbeiter, Partnerunternehmen, Mieter, Kunden und andere.</li>
    <li>Full-Service-Betreuung (Monitoring, Abrechnung, Benutzerbetreuung)</li>
    <li>Integration in ihre Unternehmensabläufe</li>
    <li>Berücksichtigung von Eigentümer/<br>Mieter-Konstellationen</li>
  </ul>

  <div class="abs benefit-box">
    <div class="benefit-head">Mit wendo-kraft Professional profitieren</div>
    <ul class="dotlist">
      <li>Effizienter Verwaltung von Lade-Infrastruktur</li>
      <li>Umfassende Full-Service-Betreuung</li>
      <li>Nahtloser Integration in Ihre kaufmännischen Prozesse</li>
      <li>Vielseitigen Abrechnungsmöglichkeiten</li>
    </ul>
  </div>

  <div class="abs contact-box">
    <div class="photo contact-photo" role="img" aria-label="Foto: Ladesäule mit grünem Ladekabel in einer Tiefgarage"></div>
    <div class="contact-body">
      <h2 class="section-head">Kontaktieren Sie uns</h2>
      <p>Erfahren Sie mehr über wendo-kraft und wie wir Ihre Abrechnungsanforderungen erfüllen können. Kontaktieren Sie uns für eine kostenlose Beratung:</p>
      <div class="phone">
        <svg width="16" height="16" viewBox="0 0 24 24" aria-hidden="true"><circle cx="12" cy="12" r="11" fill="none" stroke="var(--pink)" stroke-width="2"/><path d="M8 6.5c.6-.4 1.3-.3 1.6.3l1 2c.2.5.1 1-.3 1.3l-.8.6c.6 1.3 1.5 2.3 2.8 3l.6-.8c.3-.4.9-.5 1.3-.3l2 1c.6.3.7 1 .3 1.6-.8 1.2-2.1 1.6-3.4 1-3-1.2-5.2-3.4-6.3-6.4-.5-1.3 0-2.5 1.2-3.3z" fill="var(--purple)"/></svg>
        +49 (0) 3021 448 170
      </div>
      <div class="web-line">
        <svg width="9" height="9" viewBox="0 0 24 24" aria-hidden="true"><circle cx="12" cy="12" r="11" fill="none" stroke="var(--pink)" stroke-width="2.5"/><path d="M6 8h12v8H6z" fill="none" stroke="var(--purple)" stroke-width="2"/><path d="M6 8l6 5 6-5" fill="none" stroke="var(--purple)" stroke-width="2"/></svg>
        info@wendo-kraft.de&nbsp;|&nbsp;
        <svg width="9" height="9" viewBox="0 0 24 24" aria-hidden="true"><circle cx="12" cy="12" r="10" fill="none" stroke="var(--pink)" stroke-width="2.5"/><ellipse cx="12" cy="12" rx="4" ry="10" fill="none" stroke="var(--purple)" stroke-width="2"/><path d="M2 12h20" stroke="var(--purple)" stroke-width="2"/></svg>
        www.wendo-kraft.de
      </div>
    </div>
  </div>

  <p class="abs footer-line">wendo-kraft – Die Abrechnungslösung für Lade-Infrastruktur in Unternehmen.</p>
</section>

<section class="page page--back">
  <svg class="hero-art" width="535" height="756" viewBox="0 0 535 756">
    <defs>
      <linearGradient id="ringB" x1="0" y1="0" x2="1" y2="0">
        <stop offset="0" stop-color="#e5168e"/><stop offset="1" stop-color="#7e4cc8"/>
      </linearGradient>
      <radialGradient id="photoB" cx=".55" cy=".6" r=".6">
        <stop offset="0" stop-color="#3b6fd8"/><stop offset=".35" stop-color="#2a2d36"/>
        <stop offset=".7" stop-color="#8d8f98"/><stop offset="1" stop-color="#c9c6c2"/>
      </radialGradient>
    </defs>
    <circle cx="515" cy="-11" r="244" fill="url(#ringB)"/>
    <circle cx="515" cy="-11" r="223" fill="url(#photoB)" role="img" aria-label="Foto: blauer Ladestecker an einer Ladesäule vor unscharfen Lichtern"/>
  </svg>

  <div class="brand-name"><span class="brand-dot"></span>wendo-kraft.de</div>

  <div class="abs back-band"></div>
  <h1 class="abs display back-title">Wendo-Kraft Professional</h1>
  <div class="abs back-dark"></div>
  <p class="abs back-sub">die Funktionen im Überblick</p>

  <h2 class="abs billing-head">VERRECHNUNG VON LADEVORGÄNGEN FÜR:</h2>

  <div class="target" style="left:17px">
    <div class="target-icon"><svg width="36" height="30" viewBox="0 0 36 30" aria-hidden="true"><path d="M6 12l4-9h16l4 9h2v12h-4v4h-4v-4H12v4H8v-4H4V12z" fill="#fff"/><path d="M9.5 12l2.5-6h12l2.5 6z" fill="var(--violet)"/><rect x="7" y="16" width="5" height="3" fill="var(--violet)"/><rect x="24" y="16" width="5" height="3" fill="var(--violet)"/></svg></div>
    Fuhrpark,<br>Dienstwagen
  </div>
  <div class="divider" style="left:138px"></div>
  <div class="target" style="left:140px">
    <div class="target-icon"><svg width="38" height="30" viewBox="0 0 38 30" aria-hidden="true"><circle cx="19" cy="7" r="6" fill="#fff"/><circle cx="8" cy="10" r="4.5" fill="#fff"/><circle cx="30" cy="10" r="4.5" fill="#fff"/><path d="M10 29v-8c0-4 4-7 9-7s9 3 9 7v8z" fill="#fff"/><path d="M1 29v-6c0-3 3-5 7-5 1 0 2 .2 3 .5-1.5 1.5-2 3-2 5v5.5z M37 29v-6c0-3-3-5-7-5-1 0-2 .2-3 .5 1.5 1.5 2 3 2 5v5.5z" fill="#fff"/></svg></div>
    Mitarbeiter<br>Privatfahrzeuge
  </div>
  <div class="divider" style="left:268px"></div>
  <div class="target" style="left:265px">
    <div class="target-icon"><svg width="40" height="30" viewBox="0 0 40 30" aria-hidden="true"><g fill="#fff"><circle cx="20" cy="6" r="4"/><path d="M15 12h10v10h-2v8h-6v-8h-2z"/><circle cx="9" cy="8" r="3.2"/><path d="M5 13h8v8h-1.5v7h-5v-7H5z"/><circle cx="31" cy="8" r="3.2"/><path d="M27 13h8v8h-1.5v7h-5v-7H27z"/></g></svg></div>
    Kunden<br>und Gäste
  </div>
  <div class="divider" style="left:387px"></div>
  <div class="target" style="left:389px">
    <div class="target-icon"><svg width="34" height="34" viewBox="0 0 34 34" aria-hidden="true"><g fill="#fff"><rect x="4" y="14" width="8" height="18"/><rect x="13" y="6" width="9" height="26"/><rect x="23" y="2" width="7" height="30"/><rect x="2" y="31" width="30" height="2"/></g><g fill="var(--violet)"><rect x="6" y="17" width="2" height="3"/><rect x="6" y="23" width="2" height="3"/><rect x="16" y="10" width="2" height="3"/><rect x="16" y="16" width="2" height="3"/><rect x="16" y="22" width="2" height="3"/><rect x="25" y="7" width="2" height="4"/><rect x="25" y="14" width="2" height="4"/></g></svg></div>
    Vermieter,<br>Eigentümer
  </div>

  <div class="abs col-left">
    <h3 class="section-head">Full-Service-Betreuung für<br>sorgenfreies Management</h3>
    <p>wendo-kraft übernimmt auf Wunsch alle organisatorischen Belange bei der Verwaltung Ihrer Lade-Infrastruktur, einschließlich:</p>
    <ul class="checklist">
      <li>Monitoring</li>
      <li>Support</li>
      <li>User-Onboarding und -Support</li>
      <li>Handling von Zugangskarten</li>
      <li>Integration von firmeninternen Zugangstoken</li>
    </ul>
  </div>

  <div class="photo ref-photo" style="left:21px" role="img" aria-label="Foto: Ladesäule mit grünem Ladekabel in einer Tiefgarage"></div>
  <div class="photo ref-photo" style="left:142px;background:linear-gradient(135deg,#8f8a6e,#4f5a3a 45%,#c8c8c2 65%,#5d5a48)" role="img" aria-label="Foto: Wallbox mit grünem Ladekabel im Außenbereich"></div>

  <p class="abs back-footer">wendo-kraft – Die Abrechnungslösung<br>für Lade-Infrastruktur in Unternehmen.</p>

  <div class="abs col-right">
    <h3 class="section-head">Perfekte Integration in<br>kaufmännische Prozesse</h3>
    <p>wendo-kraft fügt sich nahtlos in die kaufmännischen Strukturen moderner Unternehmen ein und bietet:</p>
    <ul class="small-list">
      <li>Erweitertes Reporting</li>
      <li>Aufschlüsselung und Tarifierung nach Nutzergruppe</li>
      <li>Unterstützung unternehmensinterner Abrechnung und Verrechnung und/oder Zahlungseinzug durch wendo-kraft</li>
      <li>Schnittstellen zu Buchhaltung und Lohnbuchhaltung</li>
      <li>Bedarfsgerechte Anpassbarkeit</li>
    </ul>
    <h3 class="section-head gap">Besonderer Aspekt: Eigentümer-<br>Mieter-Konstellationen</h3>
    <p>Häufige Situation: Der Mieter eines Objektes benötigt Lade-Infrastruktur, der Eigentümer/ Verwalter möchte nicht zusätzlich belastet werden.</p>
    <ul class="small-list">
      <li>Unterschiedliche Betreibermodelle für verschiedene Situationen (Langzeit-Mieter vs. Kurzzeit-Mieter)</li>
      <li>Kauf-, Miet- und Leasing-Optionen</li>
      <li>Kostenneutral für Eigentümer/Verwalter durch geeignete Abrechnungsmodelle</li>
    </ul>
  </div>
</section>

</body>
</html>
```